Conference for Teenagers Needs Event Graphics

I am in need of event graphics for our upcoming event. This event, titled "Kestrel Youth Rally", is a weekend event for teenagers 11-19 years old. They hear from speakers, listen to a band, and do other fun activities. Our theme is "Together." Graphic design should have a young adult/older teen feel. Clean, not very bright colors.

Event Info:
November 6-8, 2020
Pellworth Exhibit Hall, Sioux Falls, SD
Speakers: TBD (will give name and picture before final approval)
Worship: (band name TBD before final approval)
KestrelYouthRally.com
#417KR
Our Organization Logo (attached): Lumen Forward

Once designed, I need the following graphics file sizes:
-11x17 Vertical Poster design: include all event info AND a "blank" spot/box for groups to add their own details/information. Also include the QRV logo and our organization logo Lumen Forward in someway.
-4x3 horizontal postcard: include all event info on 1 side including LumenForward logo and QRV; blank backside
-Main Graphic Slide: formatted to fit a widescreen 16x9 screen. Include event name, hashtag, QRV and Lumen Forward logo
-social media graphics for event: can incorporate some or all of the event details
-4.25x 2.75 vertical badge: include event title on front with Lumen Forward logo

Target Market(s)

Young adults or older teenagers

Requirements
Must have
• -event info
-Lumen Forward Logo & QRV logo

```html
<!DOCTYPE html>
<html lang="en">
<head>
<meta charset="utf-8">
<title>Kestrel Youth Rally – Postcard</title>
<link rel="stylesheet" href="https://fonts.googleapis.com/css2?family=Bebas+Neue&display=swap">
<style>
  :root {
    --page: #ececec;
    --teal: #22b5c6;
    --teal-text: #1fb0c4;
    --green: #5cc29a;
    --deep-teal: #1a9c9f;
    --white: #ffffff;
    --brand-blue: #1e8fd0;
    --display: "Bebas Neue", "Oswald", sans-serif;
  }
  * { box-sizing: border-box; margin: 0; padding: 0; }
  html, body { width: 1008px; height: 1200px; overflow: hidden; background: var(--page); }
  .postcard {
    position: absolute; left: 44px; top: 294px; width: 920px; height: 612px;
    background: var(--teal); overflow: hidden;
    box-shadow: 0 18px 40px rgba(0,0,0,0.16);
    font-family: var(--display); color: var(--white);
  }
  .postcard-shapes { position: absolute; inset: 0; }
  .crowd-art { position: absolute; left: 0; top: 359px; width: 356px; height: 253px;
    background: linear-gradient(180deg, #22a3a4, var(--deep-teal)); border-top-right-radius: 140px; }
  .title { position: absolute; left: 109px; line-height: 1; font-size: 92px; letter-spacing: 0; }
  .title-line-1 { top: 150px; }
  .title-line-2 { top: 220px; }
  .title-tag { position: absolute; left: 268px; top: 225px; height: 60px; padding: 0 14px;
    background: var(--white); color: var(--teal-text); font-size: 76px; line-height: 66px; }
  .title-tag::after { content: ""; position: absolute; left: 0; bottom: -9px;
    border-top: 9px solid #2b3a4a; border-left: 14px solid transparent; }
  .event-date { position: absolute; right: 360px; top: 298px; font-size: 29px; letter-spacing: 1px; }
  .event-rule { position: absolute; left: 243px; width: 317px; top: 327px; height: 2px; background: var(--white); }
  .event-venue { position: absolute; right: 360px; top: 333px; font-size: 21px; letter-spacing: 1.4px; }
  .website { position: absolute; left: 84px; top: 556px; display: flex; align-items: center; gap: 10px;
    font-size: 16px; letter-spacing: 3px; }
  .org-name { position: absolute; left: 730px; top: 46px; width: 170px; text-align: center;
    font-size: 44px; line-height: 0.95; color: var(--brand-blue); }
  .label { position: absolute; left: 598px; height: 26px; padding: 0 7px; background: var(--white);
    color: var(--teal-text); font-size: 21px; line-height: 28px; }
  .label-speakers { top: 356px; }
  .label-speakers::after { content: ""; position: absolute; left: 6px; bottom: -6px;
    border-top: 6px solid var(--white); border-right: 6px solid transparent; }
  .label-worship { top: 511px; }
  .label-worship::after { content: ""; position: absolute; right: -6px; top: 8px;
    border-left: 6px solid var(--white); border-top: 5px solid transparent; border-bottom: 5px solid transparent; }
  .speaker-photo { position: absolute; left: 598px; top: 396px; width: 96px; height: 96px; border-radius: 50%;
    border: 4px solid var(--white); background: linear-gradient(160deg, #dfe7ee, #7d8fa6 60%, #24324a); }
  .speaker-name { position: absolute; left: 712px; top: 425px; font-size: 25px; line-height: 1; }
  .speaker-role { position: absolute; left: 712px; top: 450px; font-size: 15px; letter-spacing: 1px; }
  .band-name { position: absolute; left: 712px; top: 511px; font-size: 25px; line-height: 1; }
  .hashtag { position: absolute; left: 598px; top: 558px; font-size: 16px; letter-spacing: 3px; }
</style>
</head>
<body>
<main class="postcard">
  <svg class="postcard-shapes" width="920" height="612" viewBox="0 0 920 612">
    <defs>
      <linearGradient id="green-fade" x1="0" y1="0" x2="1" y2="1">
        <stop offset="0" stop-color="#5cc29a"/>
        <stop offset="1" stop-color="#3dbcb0"/>
      </linearGradient>
      <linearGradient id="right-fade" x1="0" y1="0" x2="1" y2="1">
        <stop offset="0" stop-color="#2dbabd"/>
        <stop offset="1" stop-color="#5cc29a"/>
      </linearGradient>
    </defs>
    <circle cx="194" cy="194" r="166" fill="url(#green-fade)"/>
    <circle cx="188" cy="492" r="188" fill="url(#green-fade)"/>
    <circle cx="733" cy="202" r="235" fill="url(#right-fade)"/>
    <circle cx="859" cy="37" r="188" fill="#ffffff"/>
    <g stroke="#ffffff" stroke-linecap="round">
      <line x1="113" y1="20" x2="0" y2="103" stroke-width="2"/>
      <line x1="411" y1="3" x2="298" y2="109" stroke-width="7"/>
      <line x1="765" y1="202" x2="702" y2="261" stroke-width="7"/>
      <line x1="855" y1="227" x2="820" y2="263" stroke-width="2"/>
      <line x1="920" y1="420" x2="857" y2="482" stroke-width="2"/>
      <line x1="451" y1="555" x2="388" y2="618" stroke-width="7"/>
      <line x1="884" y1="538" x2="812" y2="618" stroke-width="7"/>
    </g>
  </svg>

  <div class="crowd-art" role="img" aria-label="Silhouette illustration of two young people facing each other"></div>

  <h1 class="event-title">
    <span class="title title-line-1">Kestrel</span>
    <span class="title title-line-2">Youth</span>
    <span class="title-tag">Rally</span>
  </h1>
  <p class="event-date">November 6-8, 2020</p>
  <div class="event-rule"></div>
  <p class="event-venue">Pellworth Exhibit Hall, Sioux Falls, SD</p>

  <p class="website">
    <svg width="20" height="20" viewBox="0 0 20 20" fill="none" stroke="#ffffff" stroke-width="1.6">
      <circle cx="10" cy="10" r="8.5"/>
      <ellipse cx="10" cy="10" rx="3.6" ry="8.5"/>
      <line x1="1.5" y1="10" x2="18.5" y2="10"/>
      <line x1="3" y1="5.5" x2="17" y2="5.5"/>
      <line x1="3" y1="14.5" x2="17" y2="14.5"/>
    </svg>
    KestrelYouthRally.com
  </p>

  <p class="org-name">Lumen<br>Forward</p>

  <span class="label label-speakers">Speakers</span>
  <div class="speaker-photo" role="img" aria-label="Portrait photo of the featured speaker"></div>
  <p class="speaker-name">Speaker's Name</p>
  <p class="speaker-role">(Designation)</p>

  <span class="label label-worship">Worship</span>
  <p class="band-name">Band's Name</p>

  <p class="hashtag">#417KR</p>
</main>
</body>
</html>
```